New Advertising Company Business Card

A two sided business card. One side with logo only and the other side with my information and maybe my logo again. Looking for something unique and creative, but not too busy. Info would include my name(Marcus Feldon), President, phone number, address, email address, and website. LOGO IS THE BLUE AND WHITE ONE.

Target Market(s)

CEO/VP Level Audience

Industry/Entity Type

Business

Contact Information for Business Card

In Description.

```html
<!DOCTYPE html>
<html lang="en">
<head>
<meta charset="UTF-8">
<title>Arcline Advertising – Business Card</title>
<link rel="stylesheet" href="https://fonts.googleapis.com/css2?family=Ubuntu:wght@400;500;700&display=swap">
<style>
  :root {
    --backdrop: #e6e2df;
    --card: #f3f3f2;
    --ink: #2a2a2c;
    --ink-soft: #3b3b3e;
    --brand-blue: #1d6ab3;
  }
  * { margin: 0; padding: 0; box-sizing: border-box; }
  html, body {
    width: 1200px;
    height: 612px;
    overflow: hidden;
    background: var(--backdrop);
    font-family: "Ubuntu", sans-serif;
  }
  .canvas {
    position: relative;
    width: 1200px;
    height: 612px;
  }
  .card {
    position: absolute;
    top: 188px;
    width: 394px;
    height: 225px;
    background: var(--card);
  }
  .card--front { left: 147px; }
  .card--back { left: 659px; }

  .brand {
    position: absolute;
    left: 0;
    right: 0;
    top: 0;
    bottom: 0;
    display: flex;
    align-items: center;
    justify-content: center;
    gap: 12px;
  }
  .brand__dot {
    width: 18px;
    height: 18px;
    border-radius: 50%;
    background: var(--brand-blue);
  }
  .brand__name {
    font-weight: 500;
    color: var(--brand-blue);
    font-size: 25px;
    letter-spacing: 0.12em;
    line-height: 1.1;
    text-transform: uppercase;
  }

  .contact {
    position: absolute;
    left: 67px;
    top: 0;
    color: var(--ink);
    text-transform: uppercase;
  }
  .contact__name {
    position: absolute;
    top: 32px;
    white-space: nowrap;
    font-weight: 700;
    font-size: 15px;
    letter-spacing: 0.16em;
  }
  .contact__title {
    position: absolute;
    top: 56px;
    white-space: nowrap;
    font-weight: 400;
    font-size: 12px;
    letter-spacing: 0.16em;
    color: var(--ink-soft);
  }
  .contact__list {
    position: absolute;
    top: 110px;
    list-style: none;
    white-space: nowrap;
    font-size: 9.5px;
    letter-spacing: 0.12em;
    color: var(--ink-soft);
  }
  .contact__item { line-height: 13px; }
  .contact__item + .contact__item { margin-top: 6.5px; }
</style>
</head>
<body>
  <main class="canvas">
    <section class="card card--front" aria-label="Card front">
      <div class="brand">
        <span class="brand__dot"></span>
        <span class="brand__name">Arcline Advertising</span>
      </div>
    </section>

    <section class="card card--back" aria-label="Card back">
      <div class="contact">
        <p class="contact__name">Marcus Feldon</p>
        <p class="contact__title">President</p>
        <ul class="contact__list">
          <li class="contact__item">+(555) 014-268-3391</li>
          <li class="contact__item">418 Harbor Avenue,<br>Suite 210 Norwell, MI 48290</li>
          <li class="contact__item">hello@arcline.co</li>
          <li class="contact__item">www.arcline.co</li>
        </ul>
      </div>
    </section>
  </main>
</body>
</html>
```